Kelvane Plumbing Business cards

Company is Kelvane Plumbing.
name Dashel Morrowby, I am a plumber, drainer, gasfitter and roofer
Mobile: 0431 906 154
Email address: info@kelvaneplumbing.example (check out my website for some ideas)
Website: www.kelvaneplumbing.example
ABN: 82 916 203 471
LIC: 604517K

I am reliable all round plumber. I am a 24 hour emergency service. Kelvane Plumbing is a professional plumbing service in the Illawarra, South Coast, Southern Sydney and Southern Highland regions of NSW. We offer a 24 hour emergency service for piece of mind to our customers. Call us now to see how we can help you. Kelvane Plumbing approaches every job with attention to detail and excellent customer service. With our superior workmanship you can be confident that the job will be done right the first time around. You can rest assured with results that are guaranteed to last.

Target Market(s)

the general public

Contact Information for Business Card

look up website for some ideas something with similar colours to logo and new modern and to catch the eye.

Colors
fdfdfd
ffffff
000000
7f7f7f
aaaaaa
33a6d7
0492cd

Requirements
Must have
• all contact details
• company- Kelvane Plumbing
• name- Dashel Morrowby
• number mobile- 0431 906 154
• Email address- info@kelvaneplumbing.example
• Website- www.kelvaneplumbing.example
• ABN- 82 916 203 471
• LIC- 604517K

```html
<!DOCTYPE html>
<html lang="en">
<head>
<meta charset="utf-8">
<title>Kelvane Plumbing — Business Cards</title>
<link rel="stylesheet" href="https://fonts.googleapis.com/css2?family=Arimo:wght@400;700&display=swap">
<style>
  :root {
    --bg: #2a2b2d;
    --card: #1f2022;
    --white: #ffffff;
    --grey: #aaaaaa;
    --mid-grey: #7f7f7f;
    --blue: #0492cd;
    --blue-light: #33a6d7;
  }
  * { box-sizing: border-box; margin: 0; padding: 0; }
  html, body {
    width: 1200px; height: 895px; overflow: hidden;
    background: var(--bg);
    font-family: "Arimo", Arial, sans-serif;
    color: var(--white);
  }
  .card {
    position: absolute;
    width: 620px; height: 354px;
    background: var(--card);
    box-shadow: 0 12px 30px rgba(0,0,0,0.45);
    overflow: hidden;
  }
  .card__stripe {
    position: absolute; left: 0; right: 0; bottom: 0;
    height: 8px; background: var(--blue);
  }

  /* Front */
  .card--front { left: 90px; top: 60px; }
  .brand {
    position: absolute; left: 0; right: 0; top: 110px;
    display: flex; align-items: center; justify-content: center; gap: 16px;
  }
  .brand__dot {
    width: 22px; height: 22px; border-radius: 50%;
    background: var(--grey);
  }
  .brand__name {
    font-weight: 700; font-size: 44px; letter-spacing: 2px;
    color: var(--grey); text-transform: uppercase;
  }
  .service-area {
    position: absolute; left: 40px; bottom: 34px;
    font-size: 15px; color: var(--white);
  }
  .service-area__state { color: var(--blue); font-weight: 700; margin-right: 4px; }

  /* Back */
  .card--back { left: 490px; top: 478px; }
  .tools-art {
    position: absolute; left: 250px; top: 28px;
    width: 120px; height: 120px;
    background: var(--blue);
    border-radius: 10px;
  }
  .owner {
    position: absolute; left: 40px; width: 218px; top: 190px;
    text-align: right;
  }
  .owner__name { font-size: 28px; color: var(--white); white-space: nowrap; }
  .owner__trades { font-size: 16px; color: var(--blue); line-height: 1.3; margin-top: 4px; }
  .divider {
    position: absolute; left: 300px; top: 178px;
    width: 2px; height: 78px; background: var(--white);
  }
  .contacts {
    position: absolute; left: 322px; top: 178px;
    list-style: none; font-size: 16px; line-height: 26px;
  }
  .contacts li { display: flex; align-items: center; gap: 10px; white-space: nowrap; }
  .contacts svg { width: 14px; height: 14px; flex: none; }
  .contacts__accent { color: var(--blue); }
  .credentials {
    position: absolute; left: 0; right: 0; top: 280px;
    text-align: center; font-size: 13px; color: var(--grey);
  }
  .credentials__label { color: var(--blue); font-weight: 700; }
  .availability {
    position: absolute; left: 0; right: 0; bottom: 26px;
    text-align: center; font-weight: 700; font-size: 15px;
  }
</style>
</head>
<body>

<section class="card card--front" aria-label="Business card front">
  <div class="brand">
    <span class="brand__dot"></span>
    <span class="brand__name">Kelvane Plumbing</span>
  </div>
  <p class="service-area">
    <span class="service-area__state">NSW</span>(Illawarra | South Coast | Southern Sydney | Southern Highland)
  </p>
  <div class="card__stripe"></div>
</section>

<section class="card card--back" aria-label="Business card back">
  <div class="tools-art" role="img" aria-label="Crossed plumbing wrenches illustration"></div>

  <div class="owner">
    <p class="owner__name">Dashel Morrowby</p>
    <p class="owner__trades">Plumber | Drainer<br>Gasfitter | Roofer</p>
  </div>

  <div class="divider"></div>

  <ul class="contacts">
    <li>
      <svg viewBox="0 0 14 14" fill="none" stroke="#0492cd" stroke-width="1.4"><rect x="3.5" y="1" width="7" height="12" rx="1.2"/><line x1="6" y1="11" x2="8" y2="11"/></svg>
      <span>0431 906 154</span>
    </li>
    <li>
      <svg viewBox="0 0 14 14" fill="none" stroke="#0492cd" stroke-width="1.4"><rect x="1" y="3" width="12" height="8"/><polyline points="1,3 7,8 13,3"/></svg>
      <span>info@<span class="contacts__accent">kelvaneplumbing</span>.example</span>
    </li>
    <li>
      <svg viewBox="0 0 14 14" fill="none" stroke="#0492cd" stroke-width="1.4"><circle cx="7" cy="6" r="4.5"/><line x1="4" y1="9.5" x2="2" y2="13"/></svg>
      <span>www.<span class="contacts__accent">kelvaneplumbing</span>.example</span>
    </li>
  </ul>

  <p class="credentials">
    <span class="credentials__label">ABN</span> 82 916 203 471 &nbsp;|&nbsp; <span class="credentials__label">LIC</span> 604517K
  </p>

  <p class="availability">24h Services</p>
  <div class="card__stripe"></div>
</section>

</body>
</html>
```